New Australian Beverage Company Needs a Bottle Label Design

We are after a bottle label design for our new aloe vera drinks called 'Bold Finch'.

There are 5+ different colourrs we would like to compliment the flavors.

We are after a logo that is simple and eye catching.
Updates

Target Market(s)

Our target market is open for all as we would like to supply our drinks to quench everyone's thirst, however our biggest customers would be the teenagers to adults up to around the age of 50.

Industry/Entity Type

It Company

Requirements
Must have
• We are after a refreshing label that catches the eyes and makes you feel like picking it up and drinking it.

```html
<!DOCTYPE html>
<html lang="en">
<head>
<meta charset="utf-8">
<title>Bold Finch Aloe Vera Drinks – Bottle Labels</title>
<link rel="stylesheet" href="https://fonts.googleapis.com/css2?family=Didact+Gothic&family=Open+Sans:ital,wght@1,700&display=swap">
<style>
  :root {
    --page: #ffffff;
    --label-white: #ffffff;
    --label-yellow: #f3ec1a;
    --label-lime: #c9de2a;
    --label-green: #6dc229;
    --ink: #1e1e1a;
    --brand-green: #1f9a3e;
    --splash-light: #dbe9f5;
    --splash-blue: #6f9cc8;
    --leaf-light: #b8d94a;
    --leaf-dark: #4f8f1c;
  }
  * { box-sizing: border-box; margin: 0; padding: 0; }
  html, body { width: 1200px; height: 1000px; overflow: hidden; background: var(--page); }
  .canvas { position: relative; width: 1200px; height: 1000px; }

  .label {
    position: absolute;
    top: 210px;
    width: 340px;
    height: 560px;
    overflow: hidden;
    background: linear-gradient(to bottom,
      var(--label-white) 0%,
      var(--label-white) 10%,
      var(--label-yellow) 45%,
      var(--label-lime) 65%,
      var(--label-green) 100%);
    font-family: "Didact Gothic", "Century Gothic", sans-serif;
    color: var(--ink);
  }
  .label--front { left: 190px; }
  .label--side  { left: 670px; }

  .splash {
    position: absolute;
    top: 0;
    width: 70px;
    height: 330px;
    background: linear-gradient(to bottom, var(--splash-blue) 0%, var(--splash-light) 55%, rgba(255,255,255,0) 100%);
    opacity: .55;
    border-radius: 0 0 35px 35px;
  }
  .splash--left  { left: 10px; }
  .splash--right { right: 10px; height: 380px; }

  .leaves {
    position: absolute;
    left: 0; right: 0; bottom: 0;
    height: 150px;
    background: linear-gradient(to top, var(--leaf-dark) 0%, var(--leaf-light) 70%, rgba(184,217,74,0) 100%);
    opacity: .85;
  }

  .brand {
    position: absolute;
    display: flex;
    align-items: center;
    gap: 10px;
    font-size: 44px;
    line-height: 1;
    color: var(--ink);
    white-space: nowrap;
  }
  .brand__dot {
    width: 30px; height: 30px;
    border-radius: 50%;
    background: var(--brand-green);
    flex: none;
  }
  .label--front .brand { left: 30px; top: 92px; }
  .label--side .brand {
    left: 58px; top: 390px;
    transform-origin: left top;
    transform: rotate(-90deg);
  }

  .product-name {
    position: absolute;
    font-size: 29px;
    line-height: 1.3;
    text-transform: uppercase;
  }
  .label--front .product-name { left: 0; right: 0; top: 215px; text-align: center; }
  .label--side .product-name { left: 135px; top: 40px; }

  .variant {
    position: absolute;
    background: var(--label-white);
    border-radius: 50%;
    font-family: "Open Sans", Arial, sans-serif;
    font-style: italic;
    font-weight: 700;
    color: var(--brand-green);
    display: flex;
    align-items: center;
    justify-content: center;
  }
  .label--front .variant { left: 75px; top: 315px; width: 200px; height: 48px; font-size: 26px; }
  .label--side .variant { left: 135px; top: 200px; width: 150px; height: 36px; font-size: 20px; }

  .volume {
    position: absolute;
    left: 0; right: 0;
    bottom: 18px;
    text-align: center;
    font-size: 22px;
    font-weight: 700;
  }
</style>
</head>
<body>
<main class="canvas">

  <section class="label label--front" aria-label="Front label">
    <div class="splash splash--left" role="img" aria-label="Splash of clear water"></div>
    <div class="splash splash--right" role="img" aria-label="Splash of clear water"></div>
    <div class="brand"><span class="brand__dot"></span>Bold Finch</div>
    <h1 class="product-name">Aloe Vera<br>Drinks</h1>
    <div class="variant">Original</div>
    <div class="leaves" role="img" aria-label="Fresh aloe vera leaves"></div>
    <div class="volume">500 ml</div>
  </section>

  <section class="label label--side" aria-label="Side label">
    <div class="splash splash--left" role="img" aria-label="Splash of clear water"></div>
    <div class="splash splash--right" role="img" aria-label="Splash of clear water"></div>
    <div class="brand"><span class="brand__dot"></span>Bold Finch</div>
    <h2 class="product-name">Aloe<br>Vera<br>Drinks</h2>
    <div class="variant">Original</div>
    <div class="leaves" role="img" aria-label="Fresh aloe vera leaves"></div>
    <div class="volume">500 ml</div>
  </section>

</main>
</body>
</html>
```